Website Design for a different kind of Business Consulting organisation needed!

We need a website design that reflects who we are, the simplicity of our consulting business and with a focus on our priority - to help our clients deliver, or execute - the "e" in Vantor-a.

Our key high level requirements are:
1) Simple and intuitive look and feel
2) Integration with all key social media platforms, chirpnet, pagebook, workring, scrollo.

10 pages, tops.
- Main page - Welcome
- About Us/ Who are Vantor-a?
- 5 services pages - Project Management, Business Process Management, Change Management, Business Analysis and Finance Systems
- Contact Us

Something like:
http://www.lmvholdings.example/

Vantor-a is a registered trademark and all Logos and other branded material are attached for reference.

So, what’s our gig: A few snippets from previous work...

We are a different kind of business consulting group. We partner with our clients to help them deliver change. We don't just provide them with the theory. We also provide them with the leadership and capability to execute the change.

We aren’t a one stop shop, and we don’t offer cookie cutter solutions. We’re a boutique consulting firm covering Project Management, Business Process Management, Change Management and Business Analytics.

Vantor-a is a professional services organisation that partners with their clients to lead the execution of strategic process and system improvement initiatives. Vantor-a combines hands on delivery with coaching in best practice methodologies and approaches to build their clients capabilities to ensure their ongoing success in project implementations.

UPDATES:

Thanks to everyone who has submitted designs so far. The standard of designs coming through is quite high, with lots of professional designs that nail the design brief. Eliminating them is proving to be quite challenging.

A few updates to the job brief:
- Please make sure the design fits on one page. We would like all of our information to be on the first page that people see without them having to scroll down
- Please ensure you include the FIVE services we offer in the design
- Please use corporate images/snapvault photos in your designs which are relevant to our business
- Please add a section for a live chirpnet feed from our chirpnet account and a link to plaza+
- Please add a section for news/updates

Also, if you are able to build a site once a design is selected, please let us know.

Thanks,

Marcela.

Target Market(s)

Our target customers are large enterprises in Australia that are growing rapidly and have recently (last 24 months) undertaken or are currently undergoing software implementations and business process improvement programs. These businesses have a turnover of $100m or above and are working hard to differentiate themselves from their competitors but are not seeing the return on investment promised by software vendors and process improvement initiatives.

Industry/Entity Type

Leadership

Requirements
Must have
• Collaboration / Training / Workshop / Consulting images all of a professional nature.
Simple, non-cluttered look with plenty of white space.

```html
<!DOCTYPE html>
<html lang="en">
<head>
<meta charset="utf-8">
<title>Vantor-a Pty Ltd – Change Management</title>
<link href="https://fonts.googleapis.com/css2?family=Open+Sans:wght@400;600;700&display=swap" rel="stylesheet">
<style>
:root{
  --brand:#0a4fa3;
  --brand-dark:#08428a;
  --brand-light:#3f7fd0;
  --grey-icon:#6d6d6d;
  --text:#3a3a3a;
  --heading-dark:#3b3b3b;
  --nav:#7d7d7d;
  --rule:#dcdcdc;
  --band:#f4f4f4;
  --white:#ffffff;
}
*{box-sizing:border-box;margin:0;padding:0}
html,body{width:759px;height:1200px;overflow:hidden;background:var(--white)}
body{position:relative;font-family:"Open Sans",Arial,sans-serif;color:var(--text)}
.top-bar{position:absolute;left:0;top:0;width:759px;height:4px;background:var(--brand)}
.logo{position:absolute;left:76px;top:16px;display:flex;align-items:center;gap:6px}
.logo-name{font-size:33px;font-weight:400;color:var(--brand);letter-spacing:0.5px;line-height:1}
.logo-dot{width:10px;height:10px;border-radius:50%;background:var(--brand);margin-top:-20px}
.social-top{position:absolute;left:583px;top:11px;display:flex;gap:7px}
.social-top span{width:20px;height:20px;border-radius:50%;background:var(--grey-icon)}
.social-top span.active{background:var(--brand)}
.main-nav{position:absolute;top:45px;left:0;width:759px;height:16px}
.main-nav a{position:absolute;top:0;font-size:11px;font-weight:600;color:var(--nav);text-decoration:none;line-height:16px}
.main-nav a.current{background:var(--brand);color:var(--white);padding:0 6px}
.dropdown{position:absolute;left:459px;top:61px;width:146px;background:var(--brand);list-style:none}
.dropdown li{height:19px;display:flex;align-items:center;gap:7px;padding-left:10px;font-size:8px;color:var(--white)}
.dropdown li.active{background:var(--brand-light)}
.dropdown i{width:9px;height:9px;border-radius:2px;background:#c9d9f0;display:block}
.hero{position:absolute;left:75px;top:72px;width:606px;height:206px;background:linear-gradient(100deg,#6f86a8 0%,#3a4250 22%,#1c1f24 45%,#24282e 100%)}
.body-copy{font-size:10.2px;line-height:15.8px;letter-spacing:-0.1px;hyphens:auto;-webkit-hyphens:auto}
.intro-icon{position:absolute;left:75px;top:301px}
.intro-title{position:absolute;left:151px;top:296px;font-size:20px;font-weight:700;color:var(--brand)}
.intro-text{position:absolute;left:151px;top:324px;width:532px}
.intro-text p+p{margin-top:4px}
.divider{position:absolute;left:75px;top:431px;width:606px;height:1px;background:var(--rule)}
.article-title{position:absolute;left:81px;top:449px;width:320px;font-size:15.5px;line-height:21px;font-weight:700;color:var(--brand)}
.article-col{position:absolute;left:81px;top:497px;width:322px}
.article-col p+p{margin-top:15.8px}
.article-photo{position:absolute;left:430px;top:457px;width:251px;height:216px;background:linear-gradient(135deg,#4a2a1c 0%,#2a1a14 40%,#7d6a60 70%,#cfc8c2 100%)}
.article-wide{position:absolute;left:81px;top:684px;width:604px}
.services-band{position:absolute;left:0;top:828px;width:759px;height:293px;background:var(--band)}
.service{position:absolute;width:300px}
.service .icon{position:absolute;left:0;top:0}
.service h3{position:absolute;left:72px;top:-4px;font-size:13.5px;font-weight:700;color:var(--heading-dark);white-space:nowrap}
.service h3.highlight{color:var(--brand)}
.service p{position:absolute;left:72px;top:14px;width:224px}
.site-footer{position:absolute;left:0;top:1121px;width:759px;height:79px;background:var(--brand);color:var(--white)}
.footer-col{position:absolute;top:15px;font-size:7.6px;line-height:12px}
.footer-col h4{font-size:8.6px;font-weight:700;letter-spacing:0.2px;line-height:12px}
.footer-social{display:flex;gap:6px;margin-top:6px}
.footer-social span{width:20px;height:20px;border-radius:50%;background:var(--white)}
.page-links{display:grid;grid-template-columns:47px auto}
.footer-logo{position:absolute;left:547px;top:12px;font-size:26px;color:var(--white);line-height:1}
.copyright{position:absolute;left:547px;top:48px;font-size:7.6px}
</style>
</head>
<body>
<div class="top-bar"></div>

<header>
  <div class="logo"><span class="logo-name">Vantor-a</span><span class="logo-dot"></span></div>
  <div class="social-top" aria-label="Social links">
    <span aria-label="plaza+"></span><span class="active" aria-label="pagebook"></span><span aria-label="workring"></span><span aria-label="chirpnet"></span>
  </div>
  <nav class="main-nav">
    <a style="left:329px">HOME</a>
    <a style="left:396px">ABOUT</a>
    <a class="current" style="left:459px">SERVICES</a>
    <a style="left:545px">PARTNERS</a>
    <a style="left:629px">CONTACT</a>
  </nav>
</header>

<div class="hero" role="img" aria-label="Hand touching a change management process diagram: assess, prepare, plan, implement and sustain the change"></div>

<ul class="dropdown">
  <li><i></i>Project Management</li>
  <li><i></i>Business Process Management</li>
  <li class="active"><i></i>Change Management</li>
  <li><i></i>Business Analysis</li>
  <li><i></i>Finance System</li>
</ul>

<section>
  <svg class="intro-icon" width="64" height="64" viewBox="0 0 64 64" aria-hidden="true">
    <circle cx="32" cy="32" r="32" fill="var(--brand)"/>
    <path d="M22 24a10 10 0 0 1 18-4" stroke="#fff" stroke-width="3" fill="none"/>
    <path d="M42 40a10 10 0 0 1-18 4" stroke="#fff" stroke-width="3" fill="none"/>
    <path d="M38 16l3 5-6 1z M26 48l-3-5 6-1z" fill="#fff"/>
    <rect x="18" y="28" width="8" height="8" fill="#fff"/><rect x="38" y="30" width="8" height="8" fill="#fff"/>
  </svg>
  <h1 class="intro-title">Change Management</h1>
  <div class="intro-text body-copy">
    <p>Sed ut perspiciatis unde omnis iste natus error sit voluptatem accusantium doloremque laudantium, totam rem aperiam, eaque ipsa quae ab illo inventore veritatis et quasi architecto beatae vitae dicta sunt explicabo.<br>Nemo enim ipsam voluptatem quia voluptas sit aspernatur aut odit aut fug set med itom.</p>
    <p>Lorem ipsum dolor sit amet, consectetur adipisicing elit, sed do eiusmod tempor incididunt ut labore et dolore ing elit, sed do eiusmod tempor incididunt ut labore et dolore in voluptate velit.</p>
  </div>
</section>

<div class="divider"></div>

<article>
  <h2 class="article-title">Formally Defining Change Management and Project Management</h2>
  <div class="article-col body-copy">
    <p>Sed ut perspiciatis unde omnis iste natus error sit voluptatem accusantium doloremque laudantium, totam rem aperiam, eaque ipsa quae ab illo inventore veritatis et quasi architecto beatae vitae dicta sunt explicabo. <b>This is bold Nemo enim ipsam</b> volupteius modi tempora incidunt ut labore et dolore magnam aliquam quaerat voluptatem. Ut enim ad minima veniam, quis nostrum exercitationem ullam corporis suscipit laboriosam?</p>
    <p>Nisi ut aliquid ex ea commodi consequatur qui dolorem ipsum quia dolor sit amet, consectetur, adipisci velit, sed quia non numquam eius modi tempora incidunt ut labore et dolore magnam aliquam</p>
  </div>
  <div class="article-photo" role="img" aria-label="Two senior businessmen in conversation at a restaurant table with wine"></div>
  <p class="article-wide body-copy">ut perspiciatis unde omnis iste natus error sit voluptatem accusantium doloremque laudantium, totam rem aperiam, eaque ipsa quae ab illo inventore veritatis et quasi architecto beatae vitae dicta sunt explicabo. <b>This is bold Nemo enim ipsam</b> volupteius modi tempora incidunt ut labore et dolore magnam aliquam quaerat voluptatem. Ut enim ad minima veniam, quis nostrum exercitationem ullam corporis suscipit laboriosam, nisi ut aliquid ex ea commodi consequatur?</p>
</article>

<section class="services-band">
  <div class="service" style="left:76px;top:31px">
    <svg class="icon" width="64" height="64" viewBox="0 0 64 64" aria-hidden="true">
      <circle cx="32" cy="32" r="32" fill="var(--grey-icon)"/>
      <rect x="28" y="16" width="8" height="8" fill="#fff"/>
      <path d="M32 24v6M20 30h24M20 30v6M32 30v6M44 30v6" stroke="#fff" stroke-width="2"/>
      <rect x="16" y="36" width="8" height="10" fill="#fff"/><rect x="28" y="36" width="8" height="10" fill="#fff"/><rect x="40" y="36" width="8" height="10" fill="#fff"/>
    </svg>
    <h3>Project Management</h3>
    <p class="body-copy">Sed ut perspiciatis unde omnis iste natus error sit voluptatem accusantium doloremque laudantium, totam rem aperiam, eaque ipsa quae ab illo inventore veritatis et quasi architecto beatae vitae dicta sunt explicabo.</p>
  </div>
  <div class="service" style="left:386px;top:31px">
    <svg class="icon" width="64" height="64" viewBox="0 0 64 64" aria-hidden="true">
      <circle cx="32" cy="32" r="32" fill="var(--brand)"/>
      <rect x="28" y="16" width="18" height="14" fill="none" stroke="#fff" stroke-width="2"/>
      <path d="M31 27v-4M35 27v-6M39 27v-3M43 27v-7" stroke="#fff" stroke-width="2"/>
      <rect x="18" y="22" width="7" height="18" fill="#fff"/>
      <rect x="26" y="38" width="22" height="8" fill="#fff"/>
    </svg>
    <h3 class="highlight">Business Process Management</h3>
    <p class="body-copy">Sed ut perspiciatis unde omnis iste natus error sit voluptatem accusantium doloremque lauab illo inventore veritatis et quasi architecto bea tae vitae dicta sunt explicabo.</p>
  </div>
  <div class="service" style="left:76px;top:157px">
    <svg class="icon" width="64" height="64" viewBox="0 0 64 64" aria-hidden="true">
      <circle cx="32" cy="32" r="32" fill="var(--grey-icon)"/>
      <rect x="26" y="17" width="22" height="16" fill="#fff"/>
      <path d="M30 30v-4M35 30v-7M40 30v-5M45 30v-9" stroke="var(--grey-icon)" stroke-width="2"/>
      <rect x="16" y="30" width="8" height="16" fill="#fff"/>
      <path d="M24 34l6-4" stroke="#fff" stroke-width="2"/>
    </svg>
    <h3>Business Analysis</h3>
    <p class="body-copy">Sed ut perspiciatis unde omnis iste natus error sit voluptatem accusantium doloremque laudantium, totam rem aperiam, eaque ipsa quae ab illo inventore veritatis .</p>
  </div>
  <div class="service" style="left:386px;top:157px">
    <svg class="icon" width="64" height="64" viewBox="0 0 64 64" aria-hidden="true">
      <circle cx="32" cy="32" r="32" fill="var(--grey-icon)"/>
      <circle cx="38" cy="26" r="7" fill="none" stroke="#fff" stroke-width="4" stroke-dasharray="3 2"/>
      <circle cx="38" cy="26" r="3" fill="#fff"/>
      <circle cx="26" cy="20" r="4" fill="none" stroke="#fff" stroke-width="3" stroke-dasharray="2 2"/>
      <rect x="20" y="36" width="12" height="12" fill="#fff"/>
    </svg>
    <h3>Finance System</h3>
    <p class="body-copy">Sed ut perspiciatis unde omnis iste natus error sit voluptatem accusantium doloremque lauab illo inventore veritatis et quasi architecto bea tae vitae dicta sunt explicabo. Nemo enim ipsam voluptatem quia voluptas sit aspernatur aut odit aut fug set med itom.</p>
  </div>
</section>

<footer class="site-footer">
  <div class="footer-col" style="left:76px">
    <h4>CONNECT WITH US</h4>
    <div>on social media network</div>
    <div class="footer-social"><span aria-label="plaza+"></span><span aria-label="pagebook"></span><span aria-label="workring"></span><span aria-label="chirpnet"></span></div>
  </div>
  <div class="footer-col" style="left:209px">
    <h4>PAGES</h4>
    <div class="page-links"><span>Home</span><span>Term &amp; Conditions</span><span>About</span><span>FAQ</span><span>Services</span><span>Partners</span></div>
  </div>
  <div class="footer-col" style="left:359px">
    <h4>CONTACT DETAILS</h4>
    <div>p: +61 3 555 010 696 &nbsp;f: +61 3 555 010 269</div>
    <div>Level 10, 18 Harbour Lane, Melbourne,</div>
    <div>Australia, 3000</div>
  </div>
  <div class="footer-logo">Vantor-a</div>
  <div class="copyright">Copyright © 2014 All Rights Reserved</div>
</footer>
</body>
</html>
```